VividoCanta hobbyist website to display and sell art.

A website to promote my artwork with the ability to sell and show many examples of my work . I have called my small hobbyist art selling business 'VividoCanta' i. Some works can be seen in my Facebook page VividoCanta . It needs to be creative and fit with my style of art. It needs to show passion!!!
I also have a business website www.brightlanewayworks.example which gives you an indication of my choice of design style.
The website will need to display art under headings of Landscape ; Portraits and Other Works ; tell the client about me the artist and my inspiration; commission works and sell art ;
My tagline is original art with colour, passion and movement. My style is impressionistic and expressive contemporary not traditional and realism.
I paint in Acrylic , Pastels and Oils.
I would like to collect information on people visiting the site so I can send them information on exhibitions; new work etc further down the track ; the ability to build landing pages ? A photo of me?
Updates

Target Market(s)

The Home Art/ Craft market- buyers of affordable but original works ; double income no kids , cool trendy lovers of abstract / impressionistic art with lots of vivid colour! For gifts or something you love for your home or office. Perhaps galleries.

Industry/Entity Type

Artists

Coding

Coded - Design and coding required

Number of Pages Required

4 page

Font styles to use
Sans Serif
Other font styles liked:
• Calibri, Comic Sans or some other fun

Requirements
Must have
• Passion , professional but modern and casual; fast and simple to use and update; clear messages ; vivid colour.
• A gallery;
• The colour will probably need to go with different coloured works as I update paintings
Nice to have
• A payment option
• Something really different and catchy
• Landing pages
Should not have
• A boring approach;

```html
<!DOCTYPE html>
<html lang="en">
<head>
<meta charset="utf-8">
<title>VividoCanta – Original Art</title>
<link href="https://fonts.googleapis.com/css2?family=Josefin+Sans:wght@400;600;700&family=Lato:wght@400;700&display=swap" rel="stylesheet">
<style>
:root{
  --blue:#3d9be9;
  --blue-light:#7cc4f7;
  --blue-dark:#2a7fd4;
  --ink:#222;
  --dark:#232323;
  --grey-bg:#efefef;
  --card-bg:#f2f2f2;
  --text:#555;
  --price:#2a6db5;
  --yellow:#f7b500;
  --white:#fff;
}
*{box-sizing:border-box;margin:0;padding:0}
html,body{width:1200px;height:3209px;overflow:hidden}
body{font-family:"Lato",sans-serif;color:var(--text);background:var(--white);position:relative}
.abs{position:absolute}
a{color:inherit;text-decoration:none}

/* top bar */
.topbar{height:38px;background:linear-gradient(var(--blue-light),var(--blue));color:var(--white);font-size:12px;display:flex;justify-content:space-between;align-items:center;padding:0 133px}
.topbar span{margin-right:18px}
/* header */
.header{height:105px;position:relative}
.brand{position:absolute;left:128px;top:22px;display:flex;align-items:center;gap:12px}
.brand-dot{width:52px;height:52px;border-radius:50%;background:var(--blue)}
.brand-name{font-family:"Josefin Sans",sans-serif;font-weight:700;font-size:30px;color:var(--ink);line-height:1}
.brand-sub{font-family:"Josefin Sans",sans-serif;font-weight:700;font-size:30px;color:var(--ink);line-height:1;padding-left:70px}
.search{position:absolute;left:629px;top:35px;width:252px;height:34px;border:1px solid #ccc;display:flex}
.search input{flex:1;border:0;padding:0 12px;font-size:12px;color:#999}
.search button{width:44px;border:0;background:var(--blue)}
.cart{position:absolute;left:903px;top:35px;height:34px;display:flex;align-items:center;border:1px solid #ccc;font-size:12px;color:var(--ink)}
.cart .label{padding:0 12px}
.cart .total{background:var(--blue);color:var(--white);height:100%;padding:0 14px;display:flex;align-items:center}
/* nav */
.nav{height:45px;background:linear-gradient(#333,#1b1b1b);display:flex;padding-left:133px}
.nav a{color:var(--white);font-family:"Josefin Sans",sans-serif;font-size:15px;display:flex;align-items:center;padding:0 36px}
.nav a.active{background:var(--blue)}
/* hero */
.hero{height:432px;position:relative;background:linear-gradient(160deg,#1f4f6b 0%,#2c8bb0 30%,#123a57 55%,#7a2a2a 75%,#d6a42a 100%);text-align:center;color:var(--white)}
.hero h1{font-family:"Josefin Sans",sans-serif;font-weight:700;font-size:72px;letter-spacing:3px;padding-top:108px}
.hero p{font-size:20px;margin-top:12px;opacity:.9}
.hero .btn{display:inline-block;margin-top:34px;width:164px;height:56px;line-height:56px;background:var(--blue);font-family:"Josefin Sans",sans-serif;font-size:14px;border-radius:3px}
.hero .arrow{position:absolute;top:186px}
/* section headings */
.brush{position:absolute;left:50%;transform:translateX(-50%);height:66px;width:420px;background:linear-gradient(90deg,rgba(61,155,233,.2),var(--blue) 18%,var(--blue) 82%,rgba(61,155,233,.2));border-radius:50% 40% 50% 40%/50%;color:var(--white);font-family:"Josefin Sans",sans-serif;font-weight:700;font-size:22px;display:flex;align-items:center;justify-content:center;text-transform:uppercase}
.brush.wide{width:540px}
/* cards */
.card{position:absolute;border:4px solid var(--ink);background:var(--card-bg);text-align:center;box-shadow:0 2px 4px rgba(0,0,0,.25)}
.card .art{margin:10px;height:calc(100% - 80px)}
.card.cat .art{height:136px}
.card.cat .title{font-family:"Josefin Sans",sans-serif;font-size:28px;color:var(--ink)}
.card.cat.active{background:var(--blue)}
.card.cat.active .title{color:var(--white)}
.card .name{font-size:17px;color:var(--ink)}
.card .price{font-size:14px;color:var(--price);margin-top:2px}
.card .price.big{font-size:19px;font-weight:700}
.card .add{display:block;margin:8px 10px 0;height:40px;line-height:40px;background:linear-gradient(var(--blue-light),var(--blue));color:var(--white);font-size:13px;font-weight:700;border-radius:3px}
.grey{position:absolute;left:0;top:1262px;width:1200px;height:629px;background:var(--grey-bg)}
/* about */
.about-img{position:absolute;left:128px;top:2539px;width:377px;height:235px;border:5px solid var(--white);box-shadow:0 0 4px rgba(0,0,0,.3);background:linear-gradient(135deg,#e9c46a,#a7b85c 45%,#6a8a3a 70%,#b55a3a)}
.about-text{position:absolute;left:528px;top:2540px;width:560px;font-size:12.5px;line-height:22px}
.about-text ul{list-style:none;margin-top:14px}
.about-text li{display:flex;align-items:center;gap:10px;margin-bottom:9px}
.readmore{display:inline-block;margin-top:4px;margin-left:6px;width:90px;height:32px;line-height:32px;background:var(--blue);color:var(--white);font-size:11px;text-align:center;border-radius:3px}
/* features */
.features{position:absolute;left:0;top:2830px;width:1200px;height:62px;background:var(--dark);color:var(--white);font-size:15px}
.features div{position:absolute;top:0;height:62px;display:flex;align-items:center;gap:12px}
/* footer */
.footer{position:absolute;left:0;top:2892px;width:1200px;height:265px;background:linear-gradient(var(--blue-light),var(--blue))}
.fcol{position:absolute;top:32px;color:var(--white)}
.fcol h4{font-family:"Josefin Sans",sans-serif;font-weight:700;font-size:19px;margin-bottom:14px}
.fcol li{list-style:none;font-size:11px;line-height:23px;opacity:.85}
.fcol p{font-size:11px;line-height:21px;opacity:.85;width:210px}
.newsinput{margin-top:12px;width:205px;height:37px;background:var(--blue-dark);border:1px solid rgba(255,255,255,.4);font-size:11px;display:flex;align-items:center;gap:8px;padding-left:12px}
.submit{margin-top:19px;width:68px;height:30px;background:var(--yellow);color:var(--white);font-size:11px;font-weight:700;display:flex;align-items:center;justify-content:center;border-radius:2px}
.cards{display:flex;gap:8px;margin-top:10px}
.cards span{width:34px;height:20px;background:var(--white);border-radius:2px}
.bottom{position:absolute;left:0;top:3157px;width:1200px;height:52px;background:var(--blue-dark);color:var(--white);font-size:11px;display:flex;align-items:center;justify-content:space-between;padding:0 80px 0 133px}
.social{display:flex;gap:16px}
.social span{width:16px;height:16px;border-radius:50%;background:var(--white)}
</style>
</head>
<body>

<div class="topbar">
  <div><span>&#9742; +000 555 0142</span><span>&#9993; hello@vividocanta.example</span></div>
  <div><span>Login</span><span>Create an Account</span></div>
</div>

<header class="header">
  <div class="brand">
    <div class="brand-dot"></div>
    <div><div class="brand-name">VividoCanta</div><div class="brand-sub" style="font-size:22px;padding-left:70px">by Mira</div></div>
  </div>
  <div class="search"><input value="Search here" aria-label="Search"><button aria-label="Search"><svg width="16" height="16" viewBox="0 0 16 16"><circle cx="7" cy="7" r="5" fill="none" stroke="#fff" stroke-width="2"/><line x1="11" y1="11" x2="15" y2="15" stroke="#fff" stroke-width="2"/></svg></button></div>
  <div class="cart"><span class="label">&#128722; Cart items ( 0 )</span><span class="total">$0</span></div>
</header>

<nav class="nav">
  <a class="active">Home</a><a>The Artist</a><a>Landscape</a><a>Animals</a><a>Portraits</a><a>How do I Buy?</a><a>Contact us</a>
</nav>

<section class="hero" role="img" aria-label="Expressive abstract seascape painting in blues, reds and yellow">
  <svg class="arrow" style="left:110px" width="24" height="34" viewBox="0 0 24 34"><path d="M20 3 L5 17 L20 31" fill="none" stroke="#fff" stroke-width="5"/></svg>
  <svg class="arrow" style="right:110px" width="24" height="34" viewBox="0 0 24 34"><path d="M4 3 L19 17 L4 31" fill="none" stroke="#fff" stroke-width="5"/></svg>
  <h1>NEW ART</h1>
  <p>A little bit of art with a lot of passion. Please visit our photo gallery.</p>
  <a class="btn">EXPLORE MORE</a>
</section>

<div class="brush" style="top:658px">Shop By Categories</div>

<div class="card cat active" style="left:133px;top:772px;width:282px;height:206px"><div class="art" role="img" aria-label="Painting of a violin with a red flower" style="background:linear-gradient(135deg,#d94a2a,#e8c070 50%,#6a4a3a)"></div><div class="title">Landscape</div></div>
<div class="card cat" style="left:458px;top:772px;width:282px;height:206px"><div class="art" role="img" aria-label="Painting of a sea turtle swimming" style="background:linear-gradient(160deg,#3a6fb0,#1e4d86 60%,#5c8fc8)"></div><div class="title">Animals</div></div>
<div class="card cat" style="left:779px;top:772px;width:282px;height:206px"><div class="art" role="img" aria-label="Painting of a sunset over the sea" style="background:linear-gradient(#5a7fa8,#c96a3a 55%,#3a2a2a)"></div><div class="title">Portraits</div></div>

<div class="card" style="left:133px;top:1031px;width:216px;height:195px"><div class="art" style="height:104px;background:linear-gradient(135deg,#9aa3a8,#c9a07a 50%,#5a5a5a)" role="img" aria-label="Modern painting of reclining figures"></div><div class="name">Modern Painting</div><div class="price">$320</div></div>
<div class="card" style="left:372px;top:1031px;width:216px;height:195px"><div class="art" style="height:104px;background:linear-gradient(135deg,#d9a050,#3a3a3a 50%,#c94a2a)" role="img" aria-label="Modern cubist painting of figures"></div><div class="name">Modern Painting</div><div class="price">$320</div></div>
<div class="card" style="left:612px;top:1031px;width:216px;height:195px"><div class="art" style="height:104px;background:linear-gradient(135deg,#8a3a2a,#d9a060 50%,#6a2a2a)" role="img" aria-label="Modern painting of dancing figures"></div><div class="name">Modern Painting</div><div class="price">$320</div></div>
<div class="card" style="left:849px;top:1031px;width:216px;height:195px"><div class="art" style="height:104px;background:linear-gradient(135deg,#c94a5a,#e0a0a0 50%,#a03a3a)" role="img" aria-label="Modern painting of a figure in a dress"></div><div class="name">Modern Painting</div><div class="price">$320</div></div>

<div class="grey"></div>
<div class="brush wide" style="top:1316px">New Art on VividoCanta</div>

<div class="card" style="left:133px;top:1431px;width:216px;height:383px"><div class="art" style="height:240px;background:linear-gradient(135deg,#c9302a,#e0a040 50%,#7a1e1e)" role="img" aria-label="Portrait painting of lovers in red"></div><div class="name">Lovers Portraits Art</div><div class="price big">$320</div><a class="add">ADD TO CART</a></div>
<div class="card" style="left:372px;top:1431px;width:216px;height:383px"><div class="art" style="height:240px;background:linear-gradient(#6a8fb8,#c96a3a 55%,#2a2a3a)" role="img" aria-label="Landscape painting of a sunset over water"></div><div class="name">Nature Landscape Art</div><div class="price big">$320</div><a class="add">ADD TO CART</a></div>
<div class="card" style="left:612px;top:1431px;width:216px;height:383px"><div class="art" style="height:240px;background:linear-gradient(135deg,#e0b040,#d9502a 50%,#5a3a2a)" role="img" aria-label="Painting of a guitar with a red flower"></div><div class="name">Guitar Portraits Art</div><div class="price big">$320</div><a class="add">ADD TO CART</a></div>
<div class="card" style="left:849px;top:1431px;width:216px;height:383px"><div class="art" style="height:240px;background:linear-gradient(160deg,#3a6fb0,#1e4d86 60%,#5c8fc8)" role="img" aria-label="Painting of a sea turtle"></div><div class="name">Animals Life Art</div><div class="price big">$320</div><a class="add">ADD TO CART</a></div>

<div class="brush wide" style="top:1952px">Featured Art on VividoCanta</div>

<div class="card" style="left:133px;top:2077px;width:282px;height:267px"><div class="art" style="height:176px;background:linear-gradient(135deg,#c9302a,#8a4a2a 50%,#e0a040)" role="img" aria-label="Portrait painting of a woman with a headscarf"></div><div class="name">Women Portraits Art</div><div class="price">$320</div></div>
<div class="card" style="left:458px;top:2077px;width:282px;height:267px"><div class="art" style="height:176px;background:linear-gradient(#d98a3a,#4a6a8a 50%,#2a3a4a)" role="img" aria-label="Painting of a camper van on a beach at sunset"></div><div class="name">Camper on Coral Beach</div><div class="price">$320</div></div>
<div class="card" style="left:779px;top:2077px;width:282px;height:267px"><div class="art" style="height:176px;background:linear-gradient(135deg,#6a8a3a,#c9a040 50%,#3a4a2a)" role="img" aria-label="Painting of a girl with a dog"></div><div class="name">Dog Story Art</div><div class="price">$320</div></div>

<div class="brush" style="top:2416px">About VividoCanta</div>

<div class="about-img" role="img" aria-label="Photo of the artist painting at an easel outdoors"></div>
<div class="about-text">
  <p>Lorem Ipsum is simply dummy text of the printing and typesetting industry. Lorem Ipsum has been the industry's standard dummy text ever since the 1500s, when an unknown printer took a galley of type and scrambled it to make a type specimen book. It has survived not only five centuries, but also the leap into electronic typesetting, remaining essentially unchanged.</p>
  <ul>
    <li><svg width="12" height="10" viewBox="0 0 12 10"><path d="M1 5 L4.5 8.5 L11 1" fill="none" stroke="#3d9be9" stroke-width="2"/></svg>Lorem Ipsum is simply dummy text of the printing and typesetting industry.</li>
    <li><svg width="12" height="10" viewBox="0 0 12 10"><path d="M1 5 L4.5 8.5 L11 1" fill="none" stroke="#3d9be9" stroke-width="2"/></svg>Lorem Ipsum is simply dummy text of the printing and typesetting industry text of the printing.</li>
    <li><svg width="12" height="10" viewBox="0 0 12 10"><path d="M1 5 L4.5 8.5 L11 1" fill="none" stroke="#3d9be9" stroke-width="2"/></svg>Lorem Ipsum is simply dummy text of the printing and typesetting industry.</li>
  </ul>
  <a class="readmore">READ MORE</a>
</div>

<div class="features">
  <div style="left:154px"><svg width="24" height="16" viewBox="0 0 24 16"><rect x="0" y="2" width="14" height="10" fill="#fff"/><path d="M14 5h5l4 4v3h-9z" fill="#fff"/><circle cx="5" cy="13" r="2.5" fill="#fff"/><circle cx="18" cy="13" r="2.5" fill="#fff"/></svg>Faster Delivery</div>
  <div style="left:374px"><svg width="18" height="18" viewBox="0 0 18 18"><rect x="1" y="6" width="16" height="11" fill="#fff"/><rect x="8" y="3" width="2" height="14" fill="#232323"/></svg>Gift Wrapping</div>
  <div style="left:573px"><svg width="16" height="18" viewBox="0 0 16 18"><rect x="1" y="8" width="14" height="10" fill="#fff"/><path d="M4 8V5a4 4 0 0 1 8 0v3" fill="none" stroke="#fff" stroke-width="2"/></svg>Secure Payment</div>
  <div style="left:772px"><svg width="20" height="18" viewBox="0 0 20 18"><path d="M1 9 L19 1 L13 17 L10 10 Z" fill="#fff"/></svg>Easy Returns</div>
  <div style="left:945px"><svg width="20" height="20" viewBox="0 0 20 20"><path d="M1 1h8l10 10-8 8L1 9z" fill="#fff"/><circle cx="5" cy="5" r="1.6" fill="#232323"/></svg>Lowest Price</div>
</div>

<footer class="footer">
  <div class="fcol" style="left:133px"><h4>QUICK LINKS</h4><ul><li>Home</li><li>The Artist</li><li>Landscape</li><li>Animals</li><li>Portraits</li><li>How do I Buy?</li><li>Contact us</li></ul></div>
  <div class="fcol" style="left:340px"><h4>ABOUT US</h4><ul><li>Our Story</li><li>Art Advisory Services</li><li>Buyer FAQ / Support</li><li>Testimonials</li><li>Seller's Guide</li><li>Artist FAQ / Support</li></ul></div>
  <div class="fcol" style="left:548px"><h4>OUR NEWSLETTER</h4><p>Sign up to our mailing list and be the first to receive the latest art offers.</p><div class="newsinput">&#9993; Enter your Mail ID</div><div class="submit">SUBMIT</div></div>
  <div class="fcol" style="left:871px"><h4>CUSTOMER SUPPORT</h4><ul><li>Why Buy from VividoCanta</li><li>Contact Us</li><li>Help Center</li><li>Buyers FAQ</li><li>Shipping and Delivery</li><li>Returns &amp; Refunds</li></ul><div class="cards"><span></span><span></span><span></span></div></div>
</footer>

<div class="bottom">
  <span>&copy; 2015 vividocanta. All right Reserved.</span>
  <div class="social"><span></span><span></span><span></span><span></span><span></span></div>
</div>

</body>
</html>
```